"Tales of Quiet Harbors" Book Cover Design

I am seeking a dynamic, modern, and professional cover design for a book focused on groundbreaking science that explores how a supplement called plasmalogens can revitalize the brain, prevent Alzheimer’s, and safeguard memories. The design should strike a balance between being visually appealing and conveying the seriousness of the topic.

Target Market(s)

The target audience includes individuals who are curious about cutting-edge science and proactive approaches to brain health, as well as those seeking to better understand how to protect their cognitive functions and memories. The cover should resonate with readers interested in health, science, and self-improvement, while reflecting the book’s informative and empowering tone.

Requirements
Must have
• The quotation across the top of the page (this is a placeholder for now, it will be changed eventually) and the author's name.
Should not have
• You don't need to use the puzzle idea!

```html
<!DOCTYPE html>
<html lang="en">
<head>
<meta charset="utf-8">
<title>Tales of Quiet Harbors — Book Cover</title>
<link href="https://fonts.googleapis.com/css2?family=Montserrat:wght@300;400;500;900&display=swap" rel="stylesheet">
<style>
  :root {
    --blue: #1f9fdc;
    --teal: #2aa9b0;
    --green: #22aa78;
    --paper: #f7f8f8;
    --white: #ffffff;
  }
  html, body {
    margin: 0;
    padding: 0;
    overflow: hidden;
    background: var(--white);
  }
  .cover {
    position: relative;
    width: 927px;
    height: 1200px;
    overflow: hidden;
    background: var(--white);
    font-family: "Montserrat", Arial, sans-serif;
  }
  .cover__texture {
    position: absolute;
    inset: 0;
    background: var(--paper);
  }
  .endorsement {
    position: absolute;
    top: 74px;
    left: 0;
    width: 100%;
    text-align: center;
    color: var(--teal);
  }
  .endorsement__quote {
    margin: 0;
    font-weight: 300;
    font-size: 27px;
    line-height: 35px;
    letter-spacing: 0.2px;
  }
  .endorsement__source {
    margin: 1px 0 0;
    font-weight: 500;
    font-size: 27px;
    line-height: 35px;
  }
  .title {
    position: absolute;
    inset: 0;
    width: 927px;
    height: 1200px;
  }
  .title__line {
    font-family: "Montserrat", Arial, sans-serif;
    font-weight: 900;
  }
  .author {
    position: absolute;
    top: 1036px;
    left: 103px;
    width: 727px;
    margin: 0;
    font-weight: 300;
    font-size: 51px;
    line-height: 56px;
    letter-spacing: 5.5px;
    white-space: nowrap;
    text-align: center;
    background: linear-gradient(90deg, var(--blue), var(--green));
    -webkit-background-clip: text;
    background-clip: text;
    color: transparent;
  }
</style>
</head>
<body>
<main class="cover">
  <div class="cover__texture" role="img" aria-label="Faint grey cracked-line texture across the background"></div>

  <header class="endorsement">
    <p class="endorsement__quote">“An Incredible guide to protecting<br>your mind and memories.”</p>
    <p class="endorsement__source">- Dr Anika Rowe, MD</p>
  </header>

  <svg class="title" viewBox="0 0 927 1200" aria-labelledby="book-title">
    <title id="book-title">Tales of Quiet Harbors</title>
    <defs>
      <linearGradient id="title-fill" x1="0" y1="0" x2="0" y2="1">
        <stop offset="0" stop-color="#1f9fdc"/>
        <stop offset="0.55" stop-color="#2aa9b0"/>
        <stop offset="1" stop-color="#22aa78"/>
      </linearGradient>
    </defs>
    <text class="title__line" x="248" y="411" font-size="229" textLength="431" lengthAdjust="spacingAndGlyphs" fill="url(#title-fill)">TALES</text>
    <text class="title__line" x="108" y="630" font-size="280" textLength="716" lengthAdjust="spacingAndGlyphs" fill="url(#title-fill)">OF QUIET</text>
    <text class="title__line" x="108" y="930" font-size="286" textLength="716" lengthAdjust="spacingAndGlyphs" fill="url(#title-fill)">HARBORS</text>

    <g role="img" aria-label="Illustration of a brain split into two halves">
      <rect x="355" y="575" width="125" height="390" rx="60" transform="rotate(18 417 770)" fill="url(#title-fill)" stroke="#ffffff" stroke-width="6"/>
    </g>
  </svg>

  <p class="author">ELLIOT MARSDEN, MD</p>
</main>
</body>
</html>
```